I need a design for Brightmoor Homes which is a custom home builder. The name on it will be Dan Porter, and I will give the phone number to the winning design. No address or website needed.

```html
<!DOCTYPE html>
<html lang="en">
<head>
<meta charset="utf-8">
<title>Brightmoor Homes – Business Card</title>
<link rel="stylesheet" href="https://fonts.googleapis.com/css2?family=Open+Sans:wght@400;600&family=Gelasio:wght@400&display=swap">
<style>
  :root {
    --page-bg: #d8d3cb;
    --card-dark: #141414;
    --card-mid: #252525;
    --accent-green: #5ec43a;
    --text-white: #f4f4f4;
    --rule-white: #e8e8e8;
  }
  * { margin: 0; padding: 0; box-sizing: border-box; }
  html, body {
    width: 1200px;
    height: 1023px;
    overflow: hidden;
    background: var(--page-bg);
  }
  .stage {
    width: 1200px;
    height: 1023px;
    display: flex;
    align-items: center;
    justify-content: center;
  }
  .business-card {
    position: relative;
    width: 840px;
    height: 480px;
    background: radial-gradient(ellipse at 45% 35%, var(--card-mid) 0%, var(--card-dark) 75%);
    box-shadow: 0 10px 30px rgba(0, 0, 0, 0.35);
    overflow: hidden;
  }
  .brand {
    position: absolute;
    left: 56px;
    top: 78px;
    display: inline-flex;
    flex-direction: column;
  }
  .brand-name {
    font-family: "Open Sans", sans-serif;
    font-weight: 600;
    font-size: 50px;
    line-height: 1;
    letter-spacing: 1px;
    color: var(--text-white);
    padding-bottom: 10px;
    border-bottom: 3px solid var(--rule-white);
    white-space: nowrap;
  }
  .brand-tagline {
    font-family: "Open Sans", sans-serif;
    font-weight: 400;
    font-size: 31px;
    line-height: 1;
    letter-spacing: 0.6px;
    color: var(--accent-green);
    margin-top: 8px;
    white-space: nowrap;
  }
  .person {
    position: absolute;
    left: 64px;
    top: 262px;
  }
  .person-name {
    font-family: "Gelasio", serif;
    font-size: 33px;
    line-height: 1.1;
    color: var(--text-white);
  }
  .person-role {
    font-family: "Gelasio", serif;
    font-size: 23px;
    line-height: 1.3;
    color: var(--accent-green);
    margin-left: 2px;
  }
  .contact {
    position: absolute;
    left: 500px;
    top: 348px;
    list-style: none;
  }
  .contact-item {
    display: flex;
    align-items: center;
    gap: 14px;
    font-family: "Gelasio", serif;
    font-size: 21px;
    color: var(--text-white);
    height: 34px;
  }
  .contact-icon {
    width: 16px;
    height: 16px;
    flex: none;
  }
  .accent-bar {
    position: absolute;
    left: 0;
    right: 0;
    bottom: 0;
    height: 18px;
    background: var(--accent-green);
  }
</style>
</head>
<body>
  <main class="stage">
    <article class="business-card">
      <header class="brand">
        <h1 class="brand-name">BRIGHTMOOR HOMES</h1>
        <p class="brand-tagline">CUSTOM HOME BUILDER</p>
      </header>

      <section class="person">
        <h2 class="person-name">Dan Porter</h2>
        <p class="person-role">Civil Engineer</p>
      </section>

      <ul class="contact">
        <li class="contact-item">
          <svg class="contact-icon" viewBox="0 0 16 16" aria-hidden="true">
            <rect x="4" y="1" width="8" height="14" rx="1.5" fill="none" stroke="var(--accent-green)" stroke-width="1.6"/>
            <rect x="7" y="12" width="2" height="1.4" fill="var(--accent-green)"/>
          </svg>
          <span>555-014-2738</span>
        </li>
        <li class="contact-item">
          <svg class="contact-icon" viewBox="0 0 16 16" aria-hidden="true">
            <rect x="1" y="3.5" width="14" height="9" fill="var(--accent-green)"/>
            <path d="M1 3.5 L8 9 L15 3.5" fill="none" stroke="var(--card-dark)" stroke-width="1.2"/>
          </svg>
          <span>dan@brightmoorhomes.com</span>
        </li>
      </ul>

      <div class="accent-bar"></div>
    </article>
  </main>
</body>
</html>
```